Sophrologist needs a cool signage at door entrance

I need signage for dr in sophrology based in Belgium (french speaking). The signed should capture the name the "Mireille Vansteelant" - "Naturopathe-Sophrologue-Reiki" and a catchphrase = (Healthy way of life)
« Fais du bien à ton corps, pour que ton âme ait envie d’y rester »
Requirements
Must have
- Hey,
Thats the instagram account for some inspiration www.instagram.com/mireille_zen_equilibre
Light colors, green, blue
Healthy way of life
Size is 45cm wide on 30 cm high
The signage will be placed in front off woof pannel

```html
<!DOCTYPE html>
<html lang="fr">
<head>
<meta charset="utf-8">
<title>Mireille Vansteelant – Enseigne</title>
<link rel="stylesheet" href="https://fonts.googleapis.com/css2?family=Arimo:wght@700&family=Great+Vibes&family=Italianno&display=swap">
<style>
  :root {
    --page: #ffffff;
    --name-blue: #4fb8d6;
    --role-green: #7cbf2c;
    --tagline-white: #ffffff;
    --tagline-lime: #c5d62a;
    --warm-orange: #f08a4b;
    --sun-peach: #ffd9a8;
    --sun-cream: #fff6e6;
    --sky-blue: #bfe3ec;
    --sky-teal: #7fc6d3;
    --wood-tan: #c9a487;
    --leaf-green: #8fb79c;
  }

  * { margin: 0; padding: 0; box-sizing: border-box; }

  html, body {
    width: 943px;
    height: 1200px;
    overflow: hidden;
    background: var(--page);
  }

  .sign {
    position: absolute;
    left: 41px;
    top: 313px;
    width: 860px;
    height: 573px;
    overflow: hidden;
  }

  .sign__scene {
    position: absolute;
    inset: 0;
    background:
      radial-gradient(ellipse 38% 50% at 32% 30%, var(--sun-cream) 0%, rgba(255,217,168,0.6) 45%, rgba(255,217,168,0) 100%),
      radial-gradient(ellipse 30% 45% at 92% 85%, rgba(143,183,156,0.75) 0%, rgba(143,183,156,0) 100%),
      radial-gradient(ellipse 18% 28% at 92% 8%, rgba(143,183,156,0.6) 0%, rgba(143,183,156,0) 100%),
      linear-gradient(180deg, rgba(255,255,255,0) 70%, rgba(201,164,135,0.75) 100%),
      linear-gradient(90deg, var(--warm-orange) 0%, #f4a06a 28%, var(--sun-peach) 48%, var(--sky-blue) 75%, var(--sky-teal) 100%);
  }

  .sign__text {
    position: absolute;
    left: 0;
    width: 100%;
    text-align: center;
    white-space: nowrap;
  }

  .sign__name {
    top: 14px;
    left: 0;
    font-family: "Italianno", cursive;
    font-size: 84px;
    line-height: 1;
    color: var(--name-blue);
  }

  .sign__roles {
    top: 106px;
    font-family: "Arimo", Arial, sans-serif;
    font-weight: 700;
    font-size: 24px;
    line-height: 1;
    color: var(--role-green);
  }

  .tagline {
    position: absolute;
    left: 290px;
    top: 178px;
    width: 420px;
    height: 220px;
    font-family: "Great Vibes", cursive;
  }

  .tagline__healthy,
  .tagline__way,
  .tagline__life {
    position: absolute;
    line-height: 1;
    white-space: nowrap;
  }

  .tagline__healthy {
    left: 0;
    top: 0;
    font-size: 80px;
    color: var(--tagline-white);
  }

  .tagline__way {
    left: 118px;
    top: 74px;
    font-size: 44px;
    color: var(--tagline-lime);
  }

  .tagline__life {
    left: 206px;
    top: 96px;
    font-size: 80px;
    color: var(--tagline-white);
  }
</style>
</head>
<body>
  <main class="sign">
    <div class="sign__scene" role="img" aria-label="Photographie : femme en posture de méditation assise en tailleur sur une terrasse en bois, lumière de soleil couchant et branches d'eucalyptus sur la droite"></div>

    <h1 class="sign__text sign__name">Mireille Vansteelant</h1>
    <p class="sign__text sign__roles">Naturopathe | Sophrologue | Reiki</p>

    <p class="tagline" aria-label="Healthy way of Life">
      <span class="tagline__healthy">Healthy</span>
      <span class="tagline__way">way of</span>
      <span class="tagline__life">Life</span>
    </p>
  </main>
</body>
</html>
```